Lotus Ember menu projecting our true authentic nature

We need a take out menu that is inviting and expresses the authentic nature of our Thai food. Also something that expresses the Thai culture. We have attached a current menu that is in need of updating. This take out menu should be something that says to potential customers "this is where I need to go." While we are Asian in nature we are specifically Thai and need to have a project that projects the Thai culture not simply Asian.

Target Market(s)

Locals and interstate traveers, college nearby, hospital personnel, mid 20s to 60s.

Industry/Entity Type

Asian Restaurant

Colors

Designer to choose colors to be used in the design.

Requirements
Must have
• Elegant, attractive features that enhance the Thai culture and provides a bit of an upscale look and appeal but that also says not overpriced for the more economical.

```html
<!DOCTYPE html>
<html lang="en">
<head>
<meta charset="utf-8">
<title>Lotus Ember — Carry Out Menu</title>
<link href="https://fonts.googleapis.com/css2?family=Kaushan+Script&family=Patrick+Hand&family=Josefin+Sans:wght@400;600&display=swap" rel="stylesheet">
<style>
:root{
  --bg:#e6e6e6;
  --gold-light:#f8e6a4;
  --gold:#f1cf6e;
  --amber:#e4a03a;
  --orange:#e98a1f;
  --maroon:#6e1f1c;
  --maroon-deep:#521512;
  --leaf:#3d8a27;
  --chili:#c8201e;
  --ink:#3b2414;
  --label:#c0262b;
  --cream:#fff8e6;
  --tag:#8a5a24;
}
*{box-sizing:border-box;margin:0;padding:0}
html,body{width:1200px;height:720px;overflow:hidden;background:var(--bg)}
body{position:relative;font-family:"Patrick Hand",cursive;color:var(--ink)}
.spread{position:absolute;top:80px;width:570px}
.spread.outside{left:20px}
.spread.inside{left:610px;top:200px}
.spread-label{font-family:"Josefin Sans",sans-serif;font-weight:400;color:var(--label);font-size:40px;letter-spacing:1px;text-align:center;margin-bottom:14px}
.panels{display:flex;height:440px;box-shadow:0 6px 14px rgba(0,0,0,.25)}
.panel{position:relative;width:190px;height:100%;overflow:hidden;
  background:radial-gradient(ellipse at 50% 45%,var(--gold-light) 0%,var(--gold) 55%,var(--amber) 100%);
  border-right:1px solid rgba(110,31,28,.25)}
.panel:last-child{border-right:none}
.ornament-top{position:absolute;top:0;left:0;right:0;height:20px;
  background:linear-gradient(180deg,var(--maroon) 0%,#8a3a1e 60%,rgba(138,58,30,0) 100%)}
.ground{position:absolute;left:0;right:0;bottom:0;height:44px}
.silhouette{position:absolute;bottom:18px;background:var(--maroon)}
.silhouette.figure{left:8px;width:34px;height:64px;border-radius:16px 16px 0 0}
.silhouette.spire{right:10px;width:22px;height:80px;border-radius:11px 11px 0 0}
.content{position:absolute;top:24px;left:10px;right:10px;bottom:40px;font-size:6px;line-height:1.22}
h3{font-family:"Kaushan Script",cursive;font-weight:400;color:var(--leaf);font-size:11px;text-align:center;margin:3px 0 1px}
.note{text-align:center;font-size:5.6px;margin-bottom:2px}
.price{color:var(--chili)}
.item{margin-bottom:1.4px}
.item .name{display:block}
.item .desc{display:block;font-size:4.8px;opacity:.85;padding-left:6px}
.list{list-style:none}
.two-col{display:grid;grid-template-columns:1fr 1fr;gap:0 6px}
.warning{text-align:center;color:var(--chili);font-size:5.4px;margin-top:4px;padding-left:36px}
.warning strong{font-size:6.4px;font-weight:400}
.info-box{position:absolute;left:0;right:0;top:280px;bottom:0;border-top:1px solid rgba(110,31,28,.35)}
.info-box p{text-align:center;font-size:5.4px;margin:6px 12px 0}
.info-box .veg{color:var(--leaf)}
.info-box .subject{color:var(--chili)}
.dish-photo{position:absolute;border-radius:50%;border:3px solid #fff;box-shadow:0 2px 4px rgba(0,0,0,.25)}
.photo-rolls{left:34px;top:360px;width:120px;height:62px;border-radius:50%;border:none;
  background:radial-gradient(ellipse,var(--cream) 30%,#c8623b 60%,var(--maroon-deep) 100%)}
.cover-brand{position:absolute;top:44px;left:0;right:0;text-align:center}
.brand-name{font-family:"Patrick Hand",cursive;font-weight:400;color:var(--maroon);font-size:30px;line-height:1;letter-spacing:.5px}
.tagline{font-size:5.4px;color:var(--tag);margin-top:6px}
.contact{position:absolute;top:118px;left:18px;right:10px;font-size:7.5px;line-height:1.35}
.contact .phone{font-size:9.5px}
.hours{margin-top:6px}
.hours b{font-weight:400;color:var(--chili);font-size:8.5px;display:block}
.orange-field{position:absolute;left:0;right:0;top:0;bottom:0}
.photo-noodle{right:8px;top:218px;width:72px;height:72px;background:radial-gradient(circle,#d86a32 0%,#f2b56a 50%,#fff 70%)}
.photo-rolls-small{left:50px;top:262px;width:40px;height:40px;background:radial-gradient(circle,#e2a15a 0%,#fff 70%)}
.photo-stirfry{left:8px;top:300px;width:70px;height:84px;border-radius:45%;background:radial-gradient(ellipse,#6f8a3a 0%,#c9813e 45%,#fff 72%)}
.photo-rice{left:86px;top:290px;width:62px;height:62px;background:radial-gradient(circle,#fff 30%,#ece7dd 55%,#fff 72%)}
.carry-out{position:absolute;right:10px;bottom:46px;width:120px;text-align:right;font-size:6.2px;line-height:1.35}
.carry-out .lead{font-size:9px}
.carry-out .web{color:#1f5fb0;font-size:6.8px}
.closing-brand{text-align:center;margin-top:6px}
.closing-brand .brand-name{font-size:20px}
.spice-key{font-size:5px;color:var(--chili);text-align:center;margin-top:2px}
</style>
</head>
<body>

<section class="spread outside">
  <h2 class="spread-label">OUTSIDE</h2>
  <div class="panels">

    <article class="panel">
      <div class="ornament-top" role="img" aria-label="Ornamental Thai border band"></div>
      <div class="content">
        <h3>Thai Dinners</h3>
        <p class="note">All Thai dinners served with steamed rice &amp; two spring rolls<br>Chicken, Pork, Tofu, Vegetarian <span class="price">9.29</span> Beef <span class="price">9.99</span><br>Large Shrimp or Squid <span class="price">12.79</span> House <span class="price">12.79</span><br>Add a House Salad <span class="price">2.89</span></p>
        <ul class="list">
          <li class="item"><span class="name">40. Pad Prig</span><span class="desc">Stir-fried with fresh chilies, onions &amp; bell peppers</span></li>
          <li class="item"><span class="name">41. Pad King</span><span class="desc">Stir-fried with fresh ginger, carrot, onion, mushrooms</span></li>
          <li class="item"><span class="name">42. Pad Prawn Wan</span><span class="desc">Sweet &amp; sour sauce, pineapple, tomato, cucumber, onion</span></li>
          <li class="item"><span class="name">43. Pad Bai Gra Prow</span><span class="desc">Basil leaves, garlic, fresh chilies, bell peppers</span></li>
          <li class="item"><span class="name">44. Pla Muk Pad Prig <span class="price">12.49</span></span><span class="desc">Squid stir-fried with chili paste &amp; basil</span></li>
          <li class="item"><span class="name">45. Pad Kor Tiam Prig Thai</span><span class="desc">Garlic, black pepper, served on a bed of lettuce</span></li>
          <li class="item"><span class="name">46. Pad Woon Sen</span><span class="desc">Glass noodles, egg, onion, cabbage, carrots</span></li>
          <li class="item"><span class="name">47. Nuer Pad Nam Mun Hoy</span><span class="desc">Oyster sauce, mushrooms, green onions</span></li>
          <li class="item"><span class="name">48. Pla Sam Rod <span class="price">9.99</span></span><span class="desc">Crispy fish fillet with spicy three flavor sauce</span></li>
          <li class="item"><span class="name">49. Pla Lad Prig <span class="price">9.99</span></span><span class="desc">Fried fish topped with chili garlic sauce</span></li>
          <li class="item"><span class="name">50. Pla Pad Prawn Wan <span class="price">9.99</span></span><span class="desc">Fried fish in Thai style sweet &amp; sour sauce</span></li>
          <li class="item"><span class="name">51. Pad Pad Ohng <span class="price">9.99</span></span><span class="desc">Fresh ginger, onion, mushrooms, celery</span></li>
          <li class="item"><span class="name">52. Pad Prik Ohng</span><span class="desc">Stir-fried with special chili sauce &amp; vegetables</span></li>
          <li class="item"><span class="name">53. Cashew Chicken, Beef, or Shrimp</span><span class="desc">Roasted cashews, bell pepper, onion, celery</span></li>
        </ul>
        <h3>Sides &amp; Sauces</h3>
        <div class="two-col">
          <span>Side of Rice <span class="price">1.49</span></span><span>Thai Chili Sauce <span class="price">.99</span></span>
          <span>Thai Sticky Rice <span class="price">2.49</span></span><span>Pineapple Sauce <span class="price">.99</span></span>
          <span>Lo Mein (Steamed) <span class="price">1.99</span></span><span>Peanut Sauce <span class="price">1.49</span></span>
          <span>Lo Mein (Stir Fried) <span class="price">2.99</span></span><span>Fries Small <span class="price">1.99</span></span>
          <span>Steamed Broccoli <span class="price">2.00</span></span><span>Extra Curry <span class="price">.50</span></span>
        </div>
        <p class="warning"><strong>ALLERGY WARNING!</strong><br>If you have an allergy to seafood or peanuts, please ask about our food preparation. We cannot guarantee that food will be free from allergens.</p>
      </div>
      <div class="silhouette figure" role="img" aria-label="Seated figure silhouette in maroon"></div>
      <svg class="ground" viewBox="0 0 190 44" preserveAspectRatio="none" aria-hidden="true">
        <path d="M0 22 C40 14 80 30 120 22 S170 14 190 20 L190 44 L0 44 Z" fill="var(--maroon)"/>
      </svg>
    </article>

    <article class="panel">
      <div class="ornament-top" role="img" aria-label="Ornamental Thai border band"></div>
      <div class="content">
        <h3>Chinese Dinners</h3>
        <p class="note">All dinners served with fried rice &amp; two spring rolls<br>Add a House Salad <span class="price">2.89</span></p>
        <ul class="list">
          <li class="item">55. Beef &amp; Broccoli <span class="price">9.99</span></li>
          <li class="item">56. Sweet &amp; Sour Chicken <span class="price">9.29</span></li>
          <li class="item">57. Pepper Steak <span class="price">9.99</span></li>
          <li class="item">58. Sweet &amp; Sour Fish <span class="price">9.99</span></li>
          <li class="item">59. Sweet &amp; Sour Shrimp <span class="price">12.49</span></li>
          <li class="item">60. Moo Goo Gai Pan <span class="price">9.29</span></li>
          <li class="item">61. Roast Pork with Mixed Vegetables <span class="price">9.29</span></li>
          <li class="item">62. Beef, Chicken, or Roast Pork Lo Mein <span class="price">9.99</span></li>
          <li class="item">63. Garlic Chicken <span class="price">9.29</span></li>
          <li class="item">64. Sesame Chicken <span class="price">9.29</span></li>
          <li class="item">65. Beef with Mixed Vegetables <span class="price">9.99</span></li>
          <li class="item">66. Mongolian Beef <span class="price">9.99</span></li>
          <li class="item">67. Chicken Broccoli <span class="price">9.29</span></li>
          <li class="item">68. Mixed Vegetables <span class="price">9.29</span></li>
        </ul>
        <h3>Deserts</h3>
        <p class="note">Thai Sticky Rice with Mango (Seasonal) <span class="price">5.99</span><br>Thai sticky rice with coconut milk &amp; sugar served with fresh ripe mango</p>
        <h3>Drinks</h3>
        <p class="note">Free Refills Except Thai Tea<br>Soft Drinks, Tea, Hot Tea, Coffee, &amp; Lemonade <span class="price">1.89</span><br>Cha-Yen (Thai Traditional Sweet Iced Tea) <span class="price">2.49</span><br>Refills <span class="price">.99</span></p>
      </div>
      <div class="info-box">
        <p>One of the key aspects of Thai cuisine is its artful blending of the four major tastes: sweet, sour, salty, bitter and spicy.</p>
        <p>Our dishes are always cooked to order; when you order, with very generous portions.</p>
        <p class="veg">All dishes may be ordered as vegetarian.</p>
        <p class="subject">**Prices subject to change without notice</p>
      </div>
      <svg class="ground" viewBox="0 0 190 44" preserveAspectRatio="none" aria-hidden="true">
        <path d="M0 24 C50 34 110 12 190 26 L190 44 L0 44 Z" fill="var(--maroon)"/>
      </svg>
      <div class="dish-photo photo-rolls" role="img" aria-label="Photo of crispy spring rolls with chili dipping sauce"></div>
    </article>

    <article class="panel">
      <div class="ornament-top" role="img" aria-label="Ornamental Thai border band"></div>
      <svg class="orange-field" viewBox="0 0 190 440" preserveAspectRatio="none" aria-hidden="true">
        <path d="M0 250 L190 180 L190 440 L0 440 Z" fill="var(--orange)"/>
        <path d="M0 395 L190 340 L190 440 L0 440 Z" fill="var(--gold-light)" opacity=".85"/>
      </svg>
      <div class="cover-brand">
        <div class="brand-name">Lotus Ember</div>
        <div class="tagline">Fresh Authentic Thai Food</div>
      </div>
      <div class="contact">
        <div>418 N. Cedar Street · Fairmont, NC 28340</div>
        <div class="phone">(910) 555-0142</div>
        <div class="hours"><b>Hours</b>Monday – Friday 11:00 am – 8:30 pm<br>Kitchen closes at 8:15 pm</div>
      </div>
      <div class="dish-photo photo-noodle" role="img" aria-label="Photo of pad thai noodles"></div>
      <div class="dish-photo photo-rolls-small" role="img" aria-label="Photo of spring rolls"></div>
      <div class="dish-photo photo-stirfry" role="img" aria-label="Photo of stir-fried vegetables"></div>
      <div class="dish-photo photo-rice" role="img" aria-label="Photo of steamed jasmine rice"></div>
      <div class="carry-out">
        <div class="lead">For Carry Out</div>
        Call ahead, or visit us at<br>
        <span class="web">www.LotusEmberKitchen.com</span><br>
        social: @lotusember
      </div>
      <svg class="ground" viewBox="0 0 190 44" preserveAspectRatio="none" aria-hidden="true">
        <path d="M0 28 C60 18 120 34 190 24 L190 44 L0 44 Z" fill="var(--maroon)"/>
      </svg>
    </article>

  </div>
</section>

<section class="spread inside">
  <h2 class="spread-label">INSIDE</h2>
  <div class="panels">

    <article class="panel">
      <div class="ornament-top" role="img" aria-label="Ornamental Thai border band"></div>
      <div class="content">
        <h3>Appetizers</h3>
        <ul class="list">
          <li class="item"><span class="name">1. Fried Spring Rolls (2) <span class="price">1.79</span> (4) <span class="price">3.59</span> (8) <span class="price">4.89</span></span><span class="desc">Rice wrapper filled with cabbage, carrots and bean thread</span></li>
          <li class="item"><span class="name">2. Fresh Spring Rolls (2) <span class="price">5.49</span></span><span class="desc">Soft rice paper with shrimp, lettuce, fresh vegetables</span></li>
          <li class="item"><span class="name">3. Fried Cheese Wontons (6) <span class="price">3.49</span> (12) <span class="price">5.89</span></span><span class="desc">Crispy wontons filled with seasoned cream cheese</span></li>
          <li class="item"><span class="name">3a. Fried Wontons Variety Pak (12) <span class="price">6.39</span></span><span class="desc">A mix of cheese and chicken wontons</span></li>
          <li class="item"><span class="name">4. Fried Chicken Wontons (6) <span class="price">4.29</span> (12) <span class="price">6.79</span></span><span class="desc">Wrapped minced chicken, deep-fried golden</span></li>
          <li class="item"><span class="name">5. Spring Meatballs (6) <span class="price">3.49</span></span><span class="desc">Seasoned meatballs served with sweet chili sauce</span></li>
          <li class="item"><span class="name">6. Tofu Tod <span class="price">4.99</span></span><span class="desc">Crispy fried tofu with our house sauce</span></li>
          <li class="item"><span class="name">7. Satay Kai (Chicken Satay) <span class="price">6.99</span></span><span class="desc">Grilled marinated chicken with peanut sauce</span></li>
          <li class="item"><span class="name">8. Shrimp Rolls (5) <span class="price">6.29</span></span><span class="desc">Whole shrimp wrapped and fried to perfection</span></li>
          <li class="item"><span class="name">9. Thai Style Chicken Wings (5) <span class="price">4.79</span> (10) <span class="price">8.99</span></span><span class="desc">Marinated wings deep-fried until golden and crisp</span></li>
          <li class="item">Thai Sampler <span class="price">11.99</span></li>
        </ul>
        <h3>Fried Rice</h3>
        <ul class="list">
          <li class="item">10a. Beef Fried Rice <span class="price">9.29</span> Thai Style <span class="price">9.99</span></li>
          <li class="item">10b. Chicken, Roast Pork, or Pork <span class="price">7.99</span> Thai Style <span class="price">8.99</span></li>
          <li class="item">10c. Vegetarian (Tofu on Request) Thai Style <span class="price">8.99</span></li>
          <li class="item">10d. Pineapple Fried Rice <span class="price">9.29</span> Thai Style <span class="price">10.29</span></li>
          <li class="item">10e. Shrimp Pineapple Fried Rice <span class="price">9.99</span> Thai Style <span class="price">10.99</span></li>
          <li class="item">11. Shrimp Fried Rice <span class="price">8.69</span> Thai Style <span class="price">9.69</span></li>
          <li class="item"><span class="name">12. House Fried Rice <span class="price">9.99</span> Thai Style <span class="price">10.99</span></span><span class="desc">Shrimp, chicken, beef, egg and onions</span></li>
        </ul>
        <p class="note">* Thai Style (egg, broccoli, tomato, carrot, &amp; onion)</p>
      </div>
      <div class="silhouette figure" role="img" aria-label="Seated figure silhouette in maroon"></div>
      <svg class="ground" viewBox="0 0 190 44" preserveAspectRatio="none" aria-hidden="true">
        <path d="M0 22 C40 14 80 30 120 22 S170 14 190 20 L190 44 L0 44 Z" fill="var(--maroon)"/>
      </svg>
    </article>

    <article class="panel">
      <div class="ornament-top" role="img" aria-label="Ornamental Thai border band"></div>
      <div class="content">
        <h3>Soups</h3>
        <ul class="list">
          <li class="item"><span class="name">13. Kang Jued Woon Sen <span class="price">8.49</span></span><span class="desc">Clear broth, glass noodles, cabbage, mushrooms</span></li>
          <li class="item"><span class="name">14. Tom Yum Koong <span class="price">10.99</span></span><span class="desc">Lemongrass soup with shrimp, mushrooms, lime juice</span></li>
          <li class="item"><span class="name">15. Tom Yum Gai <span class="price">8.49</span></span><span class="desc">Lemongrass soup with chicken, tomatoes, lime</span></li>
          <li class="item"><span class="name">16. Tom Kha Gai <span class="price">9.99</span></span><span class="desc">Coconut milk soup with chicken and galangal</span></li>
          <li class="item"><span class="name">17. Tom Kha Koong <span class="price">11.99</span></span><span class="desc">Coconut milk soup with shrimp and mushrooms</span></li>
          <li class="item"><span class="name">18. Khao Tom (Rice Soup) Chicken <span class="price">8.49</span> Shrimp <span class="price">11.49</span></span><span class="desc">Steamed rice in broth, celery, garlic, cilantro</span></li>
          <li class="item"><span class="name">19. Tofu Soup <span class="price">8.49</span></span><span class="desc">Tofu, cilantro, bean thread, Chinese cabbage</span></li>
        </ul>
        <h3>Thai Salads</h3>
        <p class="note">All salads tossed in our special spicy lime dressing</p>
        <ul class="list">
          <li class="item"><span class="name">20. Yum Nuer <span class="price">9.49</span></span><span class="desc">Grilled beef with lettuce, cucumbers, onions</span></li>
          <li class="item"><span class="name">21. Yum Pla Muk <span class="price">12.49</span></span><span class="desc">Fresh cooked squid in lemongrass dressing</span></li>
          <li class="item"><span class="name">23. Pla Koong <span class="price">12.49</span></span><span class="desc">Lime shrimp on a bed of lettuce</span></li>
          <li class="item"><span class="name">25. Yum Woon Sen <span class="price">9.49</span></span><span class="desc">Glass noodles, shrimp, chicken, celery, onion</span></li>
        </ul>
        <h3>Kid's Meal</h3>
        <p class="note">All kid's meals served with fries or rice (steamed or fried)<br>Chicken Nuggets (5) or Corn Dogs (1) <span class="price">3.99</span></p>
        <h3>Salad</h3>
        <p class="note">House Salad <span class="price">4.29</span> with meal <span class="price">2.89</span> Choice of dressing: Thai, Ranch, Italian, Honey Mustard, Thousand Island</p>
        <p class="spice-key">Indicates items are spicy. Please indicate level of spiciness.<br>Choice of Mild · Medium · Hot · Thai Hot</p>
        <div class="closing-brand">
          <div class="brand-name">Lotus Ember</div>
          <div class="tagline">Fresh Authentic Thai Food</div>
        </div>
      </div>
      <svg class="ground" viewBox="0 0 190 44" preserveAspectRatio="none" aria-hidden="true">
        <path d="M0 26 C50 34 110 14 190 26 L190 44 L0 44 Z" fill="var(--maroon)"/>
      </svg>
    </article>

    <article class="panel">
      <div class="ornament-top" role="img" aria-label="Ornamental Thai border band"></div>
      <div class="content">
        <h3>Thai Noodles</h3>
        <p class="note">Chicken, Pork, Tofu, Vegetarian <span class="price">9.29</span> Beef <span class="price">9.99</span><br>Shrimp or Squid <span class="price">12.39</span> House <span class="price">12.39</span></p>
        <ul class="list">
          <li class="item"><span class="name">27. Pad Kee Mow (Drunken Noodle)</span><span class="desc">Wide rice noodles, basil, vegetables, Thai basil</span></li>
          <li class="item"><span class="name">28. Pad Thai</span><span class="desc">Rice noodles with egg, bean sprouts, crushed peanuts</span></li>
          <li class="item"><span class="name">29. Mee Grob</span><span class="desc">Crispy egg noodles topped with Chinese vegetables</span></li>
          <li class="item"><span class="name">30. Kuay Teaw Lad Nar</span><span class="desc">Wide noodles in a soy gravy over broccoli</span></li>
          <li class="item"><span class="name">31. Pad See Ew</span><span class="desc">Stir-fried with egg, broccoli and noodles</span></li>
          <li class="item"><span class="name">32. Lad Nar Ta Lay <span class="price">13.79</span></span><span class="desc">Seafood, rice noodles, broccoli and Thai gravy</span></li>
        </ul>
        <h3>Thai Noodle Soups</h3>
        <ul class="list">
          <li class="item"><span class="name">33. Beef Noodle Soup <span class="price">8.99</span></span><span class="desc">Beef with rice noodles, bean sprouts, green onion</span></li>
          <li class="item"><span class="name">34. Pork Noodle Soup <span class="price">7.99</span></span><span class="desc">Pork with rice noodles, bean sprouts, cilantro</span></li>
          <li class="item"><span class="name">35. Roast Pork Noodle Soup <span class="price">7.99</span></span><span class="desc">Roast pork with rice noodles, greens, onions</span></li>
          <li class="item"><span class="name">36. Wonton Soup <span class="price">7.99</span></span><span class="desc">Thai style with roast pork</span></li>
        </ul>
        <h3>Thai Curries</h3>
        <p class="note">Chicken, Pork, Tofu, Vegetarian <span class="price">9.49</span> Beef <span class="price">10.49</span><br>Shrimp or Squid <span class="price">12.99</span> House <span class="price">12.99</span></p>
        <ul class="list">
          <li class="item"><span class="name">37. Gang Ped (Red Curry)</span><span class="desc">Red curry in coconut milk with bamboo shoots</span></li>
          <li class="item"><span class="name">38. Gang Kiew Wan (Green Curry)</span><span class="desc">Green curry paste, coconut milk, basil</span></li>
          <li class="item"><span class="name">38a. Gang Karee (Yellow Curry)</span><span class="desc">Yellow curry with potato, onion, coconut milk</span></li>
          <li class="item"><span class="name">38b. Gang Karee (Yellow Curry)</span><span class="desc">Massaman curry with peanuts and potatoes</span></li>
          <li class="item"><span class="name">39. Panang Curry</span><span class="desc">Sweet, rich curry in coconut milk</span></li>
        </ul>
      </div>
      <div class="silhouette spire" role="img" aria-label="Temple spire silhouette in maroon"></div>
      <svg class="ground" viewBox="0 0 190 44" preserveAspectRatio="none" aria-hidden="true">
        <path d="M0 28 C60 18 120 34 190 22 L190 44 L0 44 Z" fill="var(--maroon)"/>
      </svg>
    </article>

  </div>
</section>

</body>
</html>
```